OutBanished Sentinel and The 9 Doors of Becoming

Create a book cover for Dale Verhoffen first biography and a self-help book about The 9 Doors of Becoming.

US Harbor Lancer uses his battlefield and transition experience to guide you to success in any life challenge.

Back Cover:
Every single human being will go through a life changing event. It could be losing a job of 20 years, a divorce, being an athlete and getting hurt, or retiring from the military. These life changing events can sometime cause disastrous effects on us, our relationships, and some people never recover. This happened to Dale when he left a 12 year carrier as a Harbor Lancer with Coastal Vanguard Command. He then took the skills he learned as a Lancer and got to work solving the problem.

The OutBanished Sentinel takes us through a journey of Dale’s Transition out of Vanguard Command as he attempts to reintegrate in to civilian life. Through this Journey he found 7 different stages of transition and this book outlines them and what you can do about.

Target Market(s)

Military, Veterans

Industry/Entity Type

Military

Other font styles liked:
• Bebas Neu

Colors

Designer to choose colors to be used in the design.

Requirements
Must have
• Must have the cover image title, and my name.
• US Harbor Lancer uses his battlefield and transition experience to guide you to success in any life challenge.
Nice to have
• Would be nice to fit the device in the design somewhere maybe next to my name if it fits well.
• Back Cover:
• Every single human being will go through a life changing event. It could be losing a job of 20 years, a divorce, being an athlete and getting hurt, or retiring from the military. These life changing events can sometime cause disastrous effects on us, our relationships, and some people never recover. This happened to Dale when he left a 12 year carrier as a Harbor Lancer with Coastal Vanguard Command. He then took the skills he learned as a Lancer and got to work solving the problem.
• The OutBanished Sentinel takes us through a journey of Dale’s Transition out of Vanguard Command as he attempts to reintegrate in to civilian life. Through this Journey he found 7 different stages of transition and this book outlines them and what you can do about.
Should not have
• No Coastal Heron wheel and trident.

```html
<!DOCTYPE html>
<html lang="en">
<head>
<meta charset="utf-8">
<title>OutBanished Sentinel – Book Cover</title>
<link rel="stylesheet" href="https://fonts.googleapis.com/css2?family=Bebas+Neue&family=Source+Sans+3:wght@400;600&display=swap">
<style>
  :root {
    --page: #ffffff;
    --back-dark: #4a4740;
    --back-mid: #6e6a5f;
    --front-dark: #1d1812;
    --front-mid: #4b3d2c;
    --spine-light: #e3dcc3;
    --spine-mid: #c9bd95;
    --title-pale: #ffffff;
    --title-khaki: #d8cfa8;
    --accent-red: #b3161e;
    --gold: #c9a437;
    --spine-ink: #2a2620;
    --body-ink: #f4f1ea;
  }
  * { box-sizing: border-box; margin: 0; padding: 0; }
  html, body {
    width: 1200px; height: 843px; overflow: hidden;
    background: var(--page);
  }
  .cover-wrap { position: relative; width: 1200px; height: 843px; }

  /* Back cover */
  .back-cover {
    position: absolute; left: 35px; top: 10px; width: 546px; height: 825px;
    overflow: hidden;
  }
  .back-photo {
    position: absolute; inset: 0;
    background:
      radial-gradient(ellipse 45% 60% at 58% 38%, rgba(140,130,110,0.55), transparent 70%),
      linear-gradient(180deg, var(--back-mid) 0%, var(--back-dark) 55%, var(--back-mid) 100%);
  }
  .back-content { position: relative; padding: 48px 0 0 50px; width: 520px; }
  .back-title-top {
    font-family: "Bebas Neue", sans-serif; color: var(--title-pale);
    font-size: 42px; line-height: 0.95; letter-spacing: 0.5px;
  }
  .back-title-main {
    font-family: "Bebas Neue", sans-serif; color: var(--title-pale);
    font-size: 76px; line-height: 0.9; letter-spacing: 1px;
  }
  .back-subtitle {
    font-family: "Bebas Neue", sans-serif; color: var(--accent-red);
    font-size: 27px; line-height: 1; margin-top: 4px;
  }
  .back-blurb {
    font-family: "Source Sans 3", sans-serif; color: var(--body-ink);
    font-size: 13.6px; line-height: 18.2px; margin-top: 16px;
  }
  .back-blurb p + p { margin-top: 18px; }

  /* Spine */
  .spine {
    position: absolute; left: 581px; top: 10px; width: 41px; height: 825px;
    background: linear-gradient(90deg, var(--spine-mid), var(--spine-light) 45%, var(--spine-mid));
  }
  .spine-text {
    position: absolute; left: 50%; top: 22px;
    transform-origin: 0 0; transform: rotate(90deg) translateY(-50%);
    white-space: nowrap; display: flex; align-items: center; gap: 22px;
    font-family: "Bebas Neue", sans-serif; line-height: 1;
  }
  .spine-title { color: var(--spine-ink); font-size: 31px; letter-spacing: 1px; }
  .spine-subtitle { color: var(--accent-red); font-size: 22px; letter-spacing: 1px; }
  .spine-mark { width: 16px; height: 16px; border-radius: 50%; background: var(--gold); }
  .spine-author { color: var(--accent-red); font-size: 24px; letter-spacing: 3px; }

  /* Front cover */
  .front-cover {
    position: absolute; left: 622px; top: 10px; width: 553px; height: 825px;
    overflow: hidden;
  }
  .front-photo {
    position: absolute; inset: 0;
    background:
      radial-gradient(ellipse 40% 45% at 88% 18%, rgba(200,190,170,0.75), transparent 70%),
      radial-gradient(ellipse 45% 55% at 35% 35%, rgba(120,98,70,0.7), transparent 75%),
      linear-gradient(180deg, var(--front-mid) 0%, var(--front-dark) 60%, #2d231a 100%);
  }
  .front-tagline {
    position: absolute; left: 40px; right: 40px; top: 22px; text-align: center;
    font-family: "Source Sans 3", sans-serif; font-weight: 600; color: var(--title-khaki);
    font-size: 14px; line-height: 19px;
  }
  .front-title {
    position: absolute; left: 0; right: 0; top: 408px; text-align: center;
    font-family: "Bebas Neue", sans-serif; color: var(--title-khaki); font-weight: 400;
  }
  .front-title-top { display: block; font-size: 84px; line-height: 0.9; letter-spacing: 2px; }
  .front-title-main { display: block; font-size: 156px; line-height: 0.82; letter-spacing: 4px; }
  .front-subtitle {
    position: absolute; left: 0; right: 0; top: 620px; text-align: center;
    font-family: "Bebas Neue", sans-serif; color: var(--accent-red);
    font-size: 44px; line-height: 1; letter-spacing: 0.5px;
  }
  .front-author {
    position: absolute; left: 78px; top: 722px; display: flex; align-items: center; gap: 40px;
  }
  .author-mark { width: 48px; height: 48px; border-radius: 50%; background: var(--gold); }
  .author-name {
    font-family: "Bebas Neue", sans-serif; color: var(--accent-red);
    font-size: 40px; letter-spacing: 10px; line-height: 1;
  }
</style>
</head>
<body>
<main class="cover-wrap">

  <section class="back-cover">
    <div class="back-photo" role="img" aria-label="Faded photograph of a bearded soldier in combat gear over a weathered grey texture"></div>
    <div class="back-content">
      <h2 class="back-title-top">OutBanished</h2>
      <h2 class="back-title-main">SENTINEL</h2>
      <p class="back-subtitle">The 9 Doors of Becoming</p>
      <div class="back-blurb">
        <p>As human beings, we will inevitably go through a life-changing event at some point in our life. It could be losing a job of 20 years, finalizing a divorce, being forced to retire early because of an injury, or leaving the military. These life-changing events can have disastrous effects on us and the people around us. Some of us never work through these events and end up unhappy and stuck in life. This happened to Dale when he left a 12-year career as a Harbor Lancer with the Coastal Vanguard Command Unit. For years, he was stuck with feelings of anger, indifference, and bitterness. Until he finally decided to take action and apply the skills he learned as a Lancer and got to work on solving his personal problems.</p>
        <p>The OutBanished Sentinel takes you through the journey of Dale's transition out of the Vanguard Command as he attempted to reintegrate into the civilian world. Through this journey, he identified 9 different doors of becoming.</p>
        <p>Dale quickly realized that these 9 doors were something most veterans had to go through and he launched a non-profit that focused on helping the nation's veterans transition out of the military. Soon, Dale started developing steps to work through the doors, all aimed at the military community. However, through various speaking engagements, it became clear that Dale's ideas about the 9 doors of becoming applied to anyone, not just veterans. The doors applied to anyone that had gone through a life-altering event. This book outlines the 9 doors and how you can use them in your life. In short, the book is for anyone who has gone through a life-changing event and refuses to be a victim of circumstance. Anyone who decides to never quit, never surrender, and always move forward.</p>
      </div>
    </div>
  </section>

  <section class="spine">
    <div class="spine-text">
      <span class="spine-title">OUTBANISHED SENTINEL</span>
      <span class="spine-subtitle">THE 9 DOORS OF BECOMING</span>
      <span class="spine-mark"></span>
      <span class="spine-author">DALE VERHOFFEN</span>
    </div>
  </section>

  <section class="front-cover">
    <div class="front-photo" role="img" aria-label="Sepia photograph of a bearded soldier in sunglasses and combat gear, with a faded portrait of the author behind him"></div>
    <p class="front-tagline">US Harbor Lancer uses his battlefield and transition experience to guide you to success in any life challenge.</p>
    <h1 class="front-title">
      <span class="front-title-top">OUTBANISHED</span>
      <span class="front-title-main">SENTINEL</span>
    </h1>
    <p class="front-subtitle">THE 9 DOORS OF BECOMING</p>
    <div class="front-author">
      <span class="author-mark"></span>
      <span class="author-name">DALE VERHOFFEN</span>
    </div>
  </section>

</main>
</body>
</html>
```